Bright Lanterns Business Card

Design of business cards

Target Market(s)

We are aiming as small business owners who need anything from basic business structures, website plans, business processes and quality assurance.

Industry/Entity Type

Business

Colors

Designer to choose colors to be used in the design.

Requirements
Nice to have
• I would prefer one side of the card to use the green from the logo. Prefer to have the same font as the logo.

```html
<!DOCTYPE html>
<html lang="en">
<head>
<meta charset="UTF-8">
<title>Bright Lanterns Consulting — Business Card</title>
<link rel="stylesheet" href="https://fonts.googleapis.com/css2?family=Cinzel:wght@400;600&display=swap">
<style>
  :root {
    --lime: #b0ca0c;
    --charcoal: #4a4b4f;
    --ink: #3a3a3c;
    --paper: #ffffff;
    --backdrop: #9c9c9c;
  }
  * { margin: 0; padding: 0; box-sizing: border-box; }
  html, body {
    width: 1200px;
    height: 1000px;
    overflow: hidden;
    background: var(--backdrop);
    font-family: "Cinzel", "Times New Roman", serif;
  }
  .sheet {
    width: 1200px;
    height: 1000px;
    display: flex;
    align-items: center;
    justify-content: center;
    gap: 60px;
  }
  .card {
    width: 520px;
    height: 300px;
    position: relative;
    overflow: hidden;
    box-shadow: 0 18px 40px rgba(0,0,0,0.25);
  }
  .card--back { background: var(--lime); }
  .card--front {
    background: var(--paper);
    display: flex;
  }
  .front__band {
    width: 150px;
    height: 100%;
    background: var(--lime);
  }
  .front__rule {
    width: 6px;
    height: 100%;
    background: var(--charcoal);
  }
  .front__body {
    flex: 1;
    padding: 78px 0 0 40px;
  }
  .brand {
    display: flex;
    align-items: center;
    gap: 12px;
    color: var(--lime);
    font-weight: 600;
    font-size: 21px;
    line-height: 1.1;
    letter-spacing: 0.5px;
  }
  .brand__mark {
    width: 16px;
    height: 16px;
    background: var(--lime);
    flex: none;
  }
  .contact {
    margin-top: 42px;
    list-style: none;
    display: flex;
    flex-direction: column;
    gap: 16px;
  }
  .contact__item {
    display: flex;
    align-items: center;
    gap: 14px;
    color: var(--ink);
    font-size: 15px;
    letter-spacing: 1px;
  }
  .contact__icon { width: 18px; height: 18px; flex: none; }
</style>
</head>
<body>
  <main class="sheet">
    <section class="card card--back" aria-label="Card back"></section>

    <section class="card card--front" aria-label="Card front">
      <div class="front__band"></div>
      <div class="front__rule"></div>
      <div class="front__body">
        <div class="brand">
          <span class="brand__mark"></span>
          <span class="brand__name">Bright Lanterns<br>Consulting</span>
        </div>
        <ul class="contact">
          <li class="contact__item">
            <svg class="contact__icon" viewBox="0 0 18 18" aria-hidden="true">
              <rect x="5" y="1" width="8" height="16" rx="1.5" fill="none" stroke="var(--lime)" stroke-width="1.6"/>
              <circle cx="9" cy="14.3" r="0.9" fill="var(--lime)"/>
            </svg>
            <span>0198 765 432</span>
          </li>
          <li class="contact__item">
            <svg class="contact__icon" viewBox="0 0 18 18" aria-hidden="true">
              <rect x="1.5" y="4" width="15" height="11" rx="1" fill="var(--lime)"/>
              <path d="M2 5 L9 10.5 L16 5" fill="none" stroke="#fff" stroke-width="1.3"/>
            </svg>
            <span>hello@brightlanterns.co</span>
          </li>
        </ul>
      </div>
    </section>
  </main>
</body>
</html>
```